IT Company based on Biology Business Needs a Business Card Design

We need a business card design for a new company called 'Lumen CELL'. We develop the machine learning solutions especially focused on deep learning algorithms for biology industry. Our initial product is a vision detection on biological images to help doctors diagnose the symptoms. We would like to see designs that use the color green.

Industry/Entity Type

Business

```html
<!DOCTYPE html>
<html lang="en">
<head>
<meta charset="utf-8">
<title>Lumen CELL – Business Card</title>
<link rel="stylesheet" href="https://fonts.googleapis.com/css2?family=Open+Sans:wght@400;600&display=swap">
<style>
  :root {
    --page: #eef0ee;
    --card: #ffffff;
    --green-dark: #1e8c4c;
    --green-light: #7cc242;
    --shadow: rgba(0, 0, 0, 0.12);
  }
  * { margin: 0; padding: 0; box-sizing: border-box; }
  html, body {
    width: 1200px; height: 1200px; overflow: hidden;
    background: var(--page);
    font-family: "Open Sans", sans-serif;
  }
  .canvas {
    width: 1200px; height: 1200px;
    display: flex; flex-direction: column; align-items: center; justify-content: center;
    gap: 60px;
  }
  .card {
    position: relative;
    width: 900px; height: 514px;
    background: var(--card);
    box-shadow: 0 6px 24px var(--shadow);
    overflow: hidden;
  }
  /* Front side */
  .card-front {
    display: flex; align-items: center; justify-content: center;
  }
  .brand {
    display: flex; align-items: center; gap: 22px;
  }
  .brand-dot {
    width: 46px; height: 46px; border-radius: 50%;
    background: var(--green-light);
  }
  .brand-name {
    font-weight: 600; font-size: 84px; letter-spacing: 1px;
    color: var(--green-light);
  }
  /* Back side */
  .card-back { padding: 44px 56px; }
  .person { width: 500px; }
  .person-name {
    font-size: 56px; font-weight: 400; line-height: 1.05;
    color: var(--green-dark);
    white-space: nowrap;
  }
  .person-role {
    font-size: 34px; color: var(--green-light);
    text-align: right; line-height: 1.1;
  }
  .contact-list {
    list-style: none; margin-top: 34px;
    font-size: 25px; font-weight: 600; line-height: 1.3;
    color: var(--green-light);
    width: 460px;
  }
  .contact-item { display: flex; align-items: flex-start; gap: 14px; }
  .contact-icon { width: 24px; height: 24px; flex: none; margin-top: 5px; fill: var(--green-dark); }
  .contact-item.is-address { margin-top: 2px; }
  .brand-decoration {
    position: absolute; right: 56px; top: 196px; bottom: 36px;
    width: 270px; border-radius: 24px;
    background: linear-gradient(160deg, #9fd46a 0%, #4fae55 55%, #1e8c4c 100%);
    opacity: 0.35;
  }
</style>
</head>
<body>
<main class="canvas">
  <section class="card card-front" aria-label="Card front">
    <div class="brand">
      <span class="brand-dot"></span>
      <span class="brand-name">Lumen CELL</span>
    </div>
  </section>

  <section class="card card-back" aria-label="Card back">
    <div class="person">
      <h1 class="person-name">Your Name Here</h1>
      <p class="person-role">Designation</p>
    </div>
    <ul class="contact-list">
      <li class="contact-item">
        <svg class="contact-icon" viewBox="0 0 24 24" aria-hidden="true"><path d="M6.6 10.8a15.1 15.1 0 0 0 6.6 6.6l2.2-2.2a1 1 0 0 1 1-.25 11.4 11.4 0 0 0 3.6.57 1 1 0 0 1 1 1V20a1 1 0 0 1-1 1A17 17 0 0 1 3 4a1 1 0 0 1 1-1h3.5a1 1 0 0 1 1 1c0 1.25.2 2.45.57 3.57a1 1 0 0 1-.25 1z"/></svg>
        <span>123 456 7890</span>
      </li>
      <li class="contact-item">
        <svg class="contact-icon" viewBox="0 0 24 24" aria-hidden="true"><path d="M2 5h20v14H2z"/><path d="M3.5 6.5 12 13l8.5-6.5" fill="none" stroke="#fff" stroke-width="1.6"/></svg>
        <span>yourname@email.com</span>
      </li>
      <li class="contact-item">
        <svg class="contact-icon" viewBox="0 0 24 24" aria-hidden="true"><circle cx="12" cy="12" r="10"/><path d="M2 12h20M12 2c3 3 3 17 0 20M12 2c-3 3-3 17 0 20M4 7h16M4 17h16" fill="none" stroke="#fff" stroke-width="1.3"/></svg>
        <span>www.yourwebsiteid.com</span>
      </li>
      <li class="contact-item is-address">
        <svg class="contact-icon" viewBox="0 0 24 24" aria-hidden="true"><path d="M12 3 2 12h3v9h5v-6h4v6h5v-9h3z"/></svg>
        <span>#120, Street Name,<br>Area Name, Country<br>Pincode here</span>
      </li>
    </ul>
    <div class="brand-decoration" role="img" aria-label="Large brand mark decoration in green tones"></div>
  </section>
</main>
</body>
</html>
```